Vorna Fleet business card

I am needing a business card that at a glance shows all the services that we provide emphasizing some more than others. We are a Fleet and Compliance management company as well as a software company. We provide outsourced solutions for KPX compliance and HR services via our own software.
In addition, we do
drug testing
GPS
Cameras
Electronic DVIRS
ELD's

Target Market(s)

Transportation company owners

Industry/Entity Type

Transportation supplier

Contact Information for Business Card

the card should inform potential customers what we do

Other font styles liked:
• I have added brand guidelines. See attached

Requirements
Must have
• See description
Should not have
• Colors outside my brand guide. See attached

```html
<!DOCTYPE html>
<html lang="en">
<head>
<meta charset="utf-8">
<title>Vorna Fleet business card</title>
<link href="https://fonts.googleapis.com/css2?family=Open+Sans:wght@400;700&display=swap" rel="stylesheet">
<style>
  :root {
    --backdrop: #2b2b2b;
    --paper: #ffffff;
    --brand-red: #b8202e;
    --ink: #0d0d0d;
  }
  html, body {
    margin: 0;
    padding: 0;
    overflow: hidden;
  }
  .canvas {
    position: relative;
    width: 1200px;
    height: 582px;
    background: var(--backdrop);
    overflow: hidden;
    font-family: "Open Sans", Arial, sans-serif;
  }
  .card {
    position: absolute;
    width: 478px;
    height: 287px;
    background: var(--paper);
    box-shadow: 0 6px 14px rgba(0,0,0,0.55);
    overflow: hidden;
  }
  .card--front { left: 92px; top: 147px; }
  .card--back { left: 631px; top: 149px; }
  .card__frame {
    position: absolute;
    border: 1px solid var(--brand-red);
    box-sizing: border-box;
  }
  .card--front .card__frame { left: 21px; top: 21px; width: 436px; height: 246px; }
  .card--back .card__frame { left: 21px; top: 21px; width: 437px; height: 247px; }
  .card__band {
    position: absolute;
    left: 202px;
    top: 0;
    width: 276px;
    height: 100%;
    background: var(--brand-red);
  }
  .card--back .card__band-frame {
    position: absolute;
    left: 202px;
    top: 21px;
    width: 256px;
    height: 247px;
    border: 1px solid rgba(90,0,10,0.45);
    border-left: none;
    box-sizing: border-box;
  }
  .brand-name {
    position: absolute;
    margin: 0;
    font-weight: 700;
    color: var(--ink);
    white-space: nowrap;
    line-height: 1;
    letter-spacing: -0.5px;
  }
  .card--front .brand-name {
    left: 0; right: 0; top: 126px;
    text-align: center;
    font-size: 34px;
  }
  .card--back .brand-name {
    left: 0; width: 202px; top: 129px;
    text-align: center;
    font-size: 27px;
  }
  .services {
    position: absolute;
    left: 230px;
    top: 44px;
    margin: 0;
    padding: 0;
    list-style: none;
  }
  .services__item {
    display: flex;
    align-items: center;
    height: 30.5px;
    color: var(--paper);
    font-size: 11px;
    letter-spacing: -0.2px;
    white-space: nowrap;
  }
  .services__arrow {
    width: 8px;
    height: 8px;
    margin-right: 10px;
    flex: none;
  }
</style>
</head>
<body>
<div class="canvas">
  <section class="card card--front">
    <div class="card__frame"></div>
    <h1 class="brand-name">Vorna Fleet</h1>
  </section>

  <section class="card card--back">
    <div class="card__frame"></div>
    <div class="card__band"></div>
    <div class="card__band-frame"></div>
    <p class="brand-name">Vorna Fleet</p>
    <ul class="services">
      <li class="services__item"><svg class="services__arrow" viewBox="0 0 8 8"><path d="M0 0 L8 4 L0 8 L2 4 Z" fill="#fff"/></svg>SOLUTIONS FOR KPX COMPLIANCE</li>
      <li class="services__item"><svg class="services__arrow" viewBox="0 0 8 8"><path d="M0 0 L8 4 L0 8 L2 4 Z" fill="#fff"/></svg>HR SERVICES VIA OUR OWN SOFTWARE.</li>
      <li class="services__item"><svg class="services__arrow" viewBox="0 0 8 8"><path d="M0 0 L8 4 L0 8 L2 4 Z" fill="#fff"/></svg>DRUG TESTING</li>
      <li class="services__item"><svg class="services__arrow" viewBox="0 0 8 8"><path d="M0 0 L8 4 L0 8 L2 4 Z" fill="#fff"/></svg>GPS</li>
      <li class="services__item"><svg class="services__arrow" viewBox="0 0 8 8"><path d="M0 0 L8 4 L0 8 L2 4 Z" fill="#fff"/></svg>CAMERAS</li>
      <li class="services__item"><svg class="services__arrow" viewBox="0 0 8 8"><path d="M0 0 L8 4 L0 8 L2 4 Z" fill="#fff"/></svg>ELECTRONIC DVIRS</li>
      <li class="services__item"><svg class="services__arrow" viewBox="0 0 8 8"><path d="M0 0 L8 4 L0 8 L2 4 Z" fill="#fff"/></svg>ELD'S</li>
    </ul>
  </section>
</div>
</body>
</html>
```